Velto Works CBD Packaging Label Design. Creative Modern Minimalist. Future Work possible!!!

Creating a CBD product.Bottle size is height 84mm diameter 25mmLabel size 74mm x 38mmMatch Stick Box: 40mm x 100mm x 50mm
Pippette cap is red FYI.
NOTE: We have added a logo file but I am also paying for a new logo design. So do as you please.Need the packaging and labelling done for CBD product. Name is Velto Works. Logo is included in file below. I have also added some product packaging and design for inspiration. No need to use this but to give you an idea. Some flexibility with label dimensions. In so far as, it must fit on the base of the bottle, think eye dropper.

The last brimloft cbd oil dropper is a cool industrial design but we would prefer a design with a label.Red and white are the main colors. Minimalist, modern, clean, swiss cross in the mix are acceptable.

Also, the logo image with the textured background on the business card is part of then look we would like to package. Not a requirement but certainly a consideration.Feel free to reach out for any further questions.Below are some specs and text we need to squeeze on then packaging / labelling.

The location of the text or emphasis is NOT fixed even if it specifies the location in the description below.

Box must contain:
logo, velto Works text
Warnings-(warning sign with exclamation mark) not suitable for consumption -under 18 restricted sign?
PACKAGING TEXT (Classic rectangular)
LogoCanna Labs (below logo)10% CBD Oil (x milligram mg)10ml
Disclaimers (From dorvexi)
MEDICAL: (From dorvexi website) Disclaimer: Velto Works products are sold without any medical claims; they have not been proven to treat, relieve, nor cure any disease or medical condition. please refer to the terms and conditions (need to read these from)
CONTACT: Avoid contact during pregnancy and while nursing. Do not get in eyes, on skin, or on clothing. Get medical advice/attention if you feel unwell.ADVICE: Keep out of reach of children. Protect from sunlight. Store in a well-ventilated place. Keep cool. Refrigerate after opening.
Ingredients: Ingredients: 80% MCT oil, 20% Carmagnola Selezionata (What terpenes?check with clear horizon). 100% organic. (Check labeling) Extracted using ethanol extraction.

Side note: More information about boxing size and bottle can be seen on a competitiors site. shown below.

https://dorvexi.example/product-category/selection/

Target Market(s)

CBD oil users in Europe

Logo Text

velto works

Font styles to use
Serif
Sans Serif
Script

Requirements
Must have
• I want textured, like business card texture considered for the label. The box is a standard cardboard for the moment. Pharma grade product. I would like it to stand out in a pharmacy but not look out of place.
• We need all sides of the packaging. Use lorem ipsum if you have to. Some of the text is above though
Should not have
• Nothing that references the weed leaf. Keep that off

```html
<!DOCTYPE html>
<html lang="en">
<head>
<meta charset="utf-8">
<title>Velto Works – 10% CBD Oil Packaging</title>
<link rel="stylesheet" href="https://fonts.googleapis.com/css2?family=Montserrat:wght@800&family=Open+Sans:wght@400;600&family=Oswald:wght@500&family=Raleway:wght@400&display=swap">
<style>
  :root {
    --brand-red: #c8161d;
    --deep-red: #a80f14;
    --paper: #ffffff;
    --paper-shade: #ebebeb;
    --backdrop: #f2f2f2;
    --ink: #3b3b3b;
    --swiss-brown: #6b4a2f;
  }
  * { box-sizing: border-box; margin: 0; padding: 0; }
  html, body { width: 1200px; height: 1027px; overflow: hidden; }
  body {
    background: radial-gradient(ellipse at 55% 40%, #ffffff 0%, var(--backdrop) 70%, #e6e6e6 100%);
    position: relative;
    font-family: "Open Sans", sans-serif;
  }

  /* ---------- shared panel parts ---------- */
  .panel { position: absolute; overflow: hidden; }
  .panel-white {
    position: absolute; left: 0; right: 0; top: 0;
    background: linear-gradient(160deg, var(--paper) 0%, #f6f6f6 55%, var(--paper-shade) 100%);
  }
  .panel-red {
    position: absolute; left: 0; right: 0; bottom: 0;
    background: linear-gradient(170deg, var(--brand-red) 0%, var(--deep-red) 100%);
  }
  .band-rule { position: absolute; left: 0; right: 0; height: 3px; background: var(--paper); }

  .brand-mark { display: flex; align-items: center; justify-content: center; gap: 10px; position: absolute; left: 0; right: 0; }
  .brand-dot { border-radius: 50%; background: var(--brand-red); }
  .brand-name { font-family: "Raleway", sans-serif; font-weight: 400; color: var(--brand-red); white-space: nowrap; }

  .strength { font-family: "Montserrat", sans-serif; font-weight: 800; color: var(--brand-red); position: absolute; line-height: 1; letter-spacing: -1px; }
  .product { font-family: "Montserrat", sans-serif; font-weight: 800; position: absolute; line-height: 1; letter-spacing: -2px; }
  .product-cbd { color: var(--brand-red); }
  .product-oil { color: var(--paper); }
  .dose, .volume, .spectrum { position: absolute; color: var(--paper); font-family: "Open Sans", sans-serif; }
  .spectrum { line-height: 1; }

  /* ---------- box: side panel ---------- */
  .box-side { left: 170px; top: 150px; width: 110px; height: 740px; border-right: 1px solid #d9d9d9; }
  .box-side .panel-white { height: 478px; background: linear-gradient(180deg, #fbfbfb, #ececec); }
  .box-side .panel-red { top: 484px; }
  .box-side .band-rule { top: 478px; }
  .side-copy { position: absolute; left: 10px; right: 10px; top: 86px; font-size: 7px; line-height: 1.35; color: var(--ink); }
  .side-copy p { margin-bottom: 9px; }
  .side-copy strong { font-weight: 600; }
  .side-disclaimer { position: absolute; left: 10px; right: 10px; top: 514px; font-size: 5.5px; line-height: 1.4; color: #f3c9ca; }

  /* ---------- box: front panel ---------- */
  .box-front { left: 280px; top: 150px; width: 300px; height: 740px; box-shadow: 6px 8px 18px rgba(0,0,0,.08); }
  .box-front .panel-white { height: 478px; }
  .box-front .panel-red { top: 484px; }
  .box-front .band-rule { top: 478px; }
  .box-front .brand-mark { top: 140px; }
  .box-front .brand-dot { width: 16px; height: 16px; }
  .box-front .brand-name { font-size: 34px; }

  .swiss-made { position: absolute; top: 282px; left: 0; right: 0; display: flex; align-items: center; justify-content: center; gap: 6px;
    font-family: "Oswald", sans-serif; font-weight: 500; font-size: 14px; color: var(--swiss-brown); }
  .swiss-made .rule { width: 10px; height: 1px; background: var(--swiss-brown); }

  .box-front .strength { left: 28px; top: 354px; font-size: 40px; }
  .box-front .product-cbd { left: 26px; top: 392px; font-size: 78px; }
  .box-front .product-oil { left: 30px; top: 488px; font-size: 78px; }
  .box-front .dose { left: 32px; top: 572px; font-size: 24px; }
  .box-front .volume { left: 32px; top: 670px; font-size: 28px; }
  .box-front .spectrum { left: 194px; top: 648px; font-size: 21px; }

  /* ---------- bottle label ---------- */
  .bottle-label { left: 700px; top: 270px; width: 300px; height: 490px; box-shadow: 6px 8px 18px rgba(0,0,0,.08); }
  .bottle-label .panel-white { height: 262px; }
  .bottle-label .panel-red { top: 268px; }
  .bottle-label .band-rule { top: 262px; }
  .bottle-label .brand-mark { top: 74px; }
  .bottle-label .brand-dot { width: 13px; height: 13px; }
  .bottle-label .brand-name { font-size: 28px; }
  .bottle-label .strength { left: 46px; top: 156px; font-size: 34px; }
  .bottle-label .product-cbd { left: 44px; top: 186px; font-size: 68px; }
  .bottle-label .product-oil { left: 48px; top: 276px; font-size: 68px; }
  .bottle-label .dose { left: 50px; top: 356px; font-size: 21px; }
  .bottle-label .volume { left: 22px; top: 420px; font-size: 23px; }
  .bottle-label .spectrum { left: 160px; top: 412px; font-size: 19px; }
</style>
</head>
<body>

  <!-- Box side panel -->
  <section class="panel box-side" aria-label="Box side panel">
    <div class="panel-white"></div>
    <div class="band-rule"></div>
    <div class="panel-red"></div>
    <div class="side-copy">
      <p>Avoid contact during pregnancy and while nursing. Do not get in eyes, on skin, or on clothing. Get medical advice/attention if you feel unwell.</p>
      <p>Keep out of reach of children.</p>
      <p>Protect from sunlight.</p>
      <p>Store in a well-ventilated place. Keep cool. Refrigerate after opening.</p>
      <p><strong>Ingredients:</strong> 80% MCT oil, 20% Carmagnola Selezionata.</p>
      <p><strong>100% organic.</strong></p>
      <p>Extracted using ethanol extraction.</p>
    </div>
    <p class="side-disclaimer">Disclaimer: Velto Works products are sold without any medical claims; they have not been proven to treat, relieve, nor cure any disease or medical condition. Please see terms.</p>
  </section>

  <!-- Box front panel -->
  <section class="panel box-front" aria-label="Box front panel">
    <div class="panel-white"></div>
    <div class="band-rule"></div>
    <div class="panel-red"></div>

    <div class="brand-mark">
      <span class="brand-dot"></span>
      <span class="brand-name">Velto Works</span>
    </div>

    <div class="swiss-made">
      <span>SWISS</span><span class="rule"></span>
      <svg width="28" height="26" viewBox="0 0 28 26" aria-hidden="true">
        <rect width="28" height="26" rx="4" fill="var(--brand-red)"/>
        <rect x="11" y="5" width="6" height="16" fill="#fff"/>
        <rect x="6" y="10" width="16" height="6" fill="#fff"/>
      </svg>
      <span class="rule"></span><span>MADE</span>
    </div>

    <div class="strength">10%</div>
    <div class="product product-cbd">CBD</div>
    <div class="product product-oil">OIL</div>
    <div class="dose">(500mg)</div>
    <div class="volume">10ml</div>
    <div class="spectrum">Full<br>Spectrum</div>
  </section>

  <!-- Bottle label -->
  <section class="panel bottle-label" aria-label="Bottle label">
    <div class="panel-white"></div>
    <div class="band-rule"></div>
    <div class="panel-red"></div>

    <div class="brand-mark">
      <span class="brand-dot"></span>
      <span class="brand-name">Velto Works</span>
    </div>

    <div class="strength">10%</div>
    <div class="product product-cbd">CBD</div>
    <div class="product product-oil">OIL</div>
    <div class="dose">(500mg)</div>
    <div class="volume">10ml</div>
    <div class="spectrum">Full<br>Spectrum</div>
  </section>

</body>
</html>
```